BWK Website

We need a website for a company based in Doha Qatar called Crewline Partners Global. It is a global recruitment company, that specializes in both mass recruitment and headhunting. The company is the number 1 one stop shop for recruitment in Qatar. It recruits from all over the world Europe, Asia, Americas, Middle East, Africa for Qatar.
Updates

Target Market(s)

Multinational companies, fortune 500 company CEO's, any top earning companies that are looking for a large number of employees or headhunting employees.
Also for candidates looking for companies to work in Qatar.

Industry/Entity Type

Shop

Colors
ffffff

Requirements
Must have
• Most important qualities the website needs to have:
Clean
Modern
Elegant
Professional
Less Tabs
Minimalisitc

Some examples, I would like you to follow are here:
http://www.velorin.ca/
http://www.trobeckhall.com/
https://quillantro.com/match#

The main color should be white and it has to have a very stylish, modern and cool look. While being minimalistic. I do not want too many tabs. I want it to be simplistic to understand. the only place where the pink logo color is should be in the logo. The logo color should not be anywhere else. It has to be absolutely sleek. Please follow the example websites that I have provided.

I will send the contact details you need to add later. There is no need for a log in page.

Whatever you think that may be important for a recruitment site do suggest. But there is no need for a log in area as we are a different kind of recruitment company.

There should be an area for testimonials from clients. There should also be an area for news flash for the latest countries we are hiring from and the latest companies we are hiring for and the latest positions we are looking for.

Show me the best please. Whoever gives me the best, I will give them an order for the 2nd website too.

Nice to have
• I have included a powerpoint to explain more!

```html
<!DOCTYPE html>
<html lang="en">
<head>
<meta charset="utf-8">
<title>Crewline Partners Global</title>
<link rel="stylesheet" href="https://fonts.googleapis.com/css2?family=Arimo:ital,wght@0,400;0,700;1,400&display=swap">
<style>
:root{
  --brand:#a3175f;
  --ink:#333;
  --text:#666;
  --muted:#8a8a8a;
  --faint:#b5b5b5;
  --line:#e3e3e3;
  --page:#f7f7f7;
  --band:#f3f3f3;
  --white:#fff;
  --dark:#333;
  --accent:#5c8fb8;
}
*{margin:0;padding:0;box-sizing:border-box}
html,body{width:1200px;height:1000px;overflow:hidden}
body{position:relative;background:var(--page);font-family:'Arimo',Arial,sans-serif;color:var(--text)}
.abs{position:absolute}

/* hero */
.hero{left:253px;top:0;width:707px;height:343px;background:linear-gradient(90deg,#f4f4f4 0%,#e2e2e2 30%,#cfcfcf 55%,#ededed 75%,#d8d8d8 100%)}
.hero-portrait{left:700px;top:0;width:255px;height:343px;background:radial-gradient(ellipse at 55% 40%,#9a9a9a 0%,#bdbdbd 45%,#e4e4e4 80%,transparent 100%)}
.brand{display:flex;align-items:center;gap:6px}
.brand-dot{width:14px;height:14px;border-radius:50%;background:var(--brand)}
.brand-name{color:var(--brand);font-weight:700;line-height:1.05}
.hero-brand{left:264px;top:46px}
.hero-brand .brand-name{font-size:11px;width:80px}
.hero-title{left:264px;top:125px;font-size:18px;color:#555;line-height:21px}
.hero-title b{font-weight:700}
.hero-arrows{left:262px;top:174px;display:flex;gap:8px}

/* nav */
.navbar{left:0;top:292px;width:1200px;height:40px;background:var(--white)}
.nav-brand{left:262px;top:298px}
.nav-brand .brand-name{font-size:14px;width:130px}
.nav{left:445px;top:292px;display:flex;height:40px}
.nav a{display:block;height:40px;line-height:40px;font-size:8px;color:var(--muted);text-decoration:none;text-align:center;border-right:1px solid var(--line)}
.nav a.active{background:var(--dark);color:var(--white);font-weight:700}
.social{top:304px;width:16px;height:16px;border-radius:50%;background:#777}
.nav-tab-foot{left:445px;top:343px;width:60px;height:3px;background:var(--dark)}

/* partners */
.partners{left:0;top:348px;width:1200px;height:47px;background:var(--white);border-top:1px solid var(--line);border-bottom:1px solid var(--line)}
.partner-row{left:282px;top:366px;display:flex;gap:7px;align-items:center}
.partner{height:13px;background:#d2d2d2;border-radius:2px}

/* welcome */
.welcome{left:0;top:396px;width:1200px;height:99px;background:var(--band);text-align:center}
.welcome h1{margin-top:21px;font-size:14px;font-weight:400;color:#777;letter-spacing:.3px}
.welcome p{width:440px;margin:14px auto 0;font-size:8px;line-height:11px;color:var(--muted)}

/* features */
.features{left:0;top:495px;width:1200px;height:151px;background:var(--white);border-bottom:2px solid var(--line)}
.feature-frame{left:253px;top:517px;width:182px;height:105px;border:1px solid var(--line);padding:4px;background:var(--white)}
.feature-image{width:100%;height:100%;background:radial-gradient(circle at 75% 55%,#9d9d9d 0%,#7d7d7d 35%,#a9a9a9 60%,#c9c9c9 100%)}
.feature h2{font-size:12px;font-weight:400;color:#777;margin-bottom:9px}
.feature p{font-size:7.5px;line-height:13.5px;color:var(--muted)}
.read-more{font-size:6.5px;font-weight:700;color:var(--muted);letter-spacing:.3px}
.vrule{top:518px;width:1px;height:100px;background:var(--line)}

/* lower columns */
.col-title{display:flex;align-items:center;gap:10px;font-size:11px;color:#666}
.card{left:253px;width:242px;height:65px;background:var(--white);border:1px solid var(--line)}
.avatar{position:absolute;left:6px;top:7px;width:49px;height:49px;border-radius:50%;background:radial-gradient(circle at 50% 40%,#cfcfcf,#8e8e8e)}
.quote{position:absolute;left:65px;top:11px;width:170px;font-size:7.5px;line-height:10px;color:#666}
.person{position:absolute;left:65px;top:40px;font-size:7.5px;color:var(--ink)}
.date{left:515px;width:53px;height:65px;background:var(--white);border:1px solid var(--line);text-align:center;padding-top:17px}
.date b{display:block;font-size:16px;font-weight:400;color:#999}
.date span{font-size:6.5px;color:var(--faint)}
.news{left:580px;width:180px}
.news .quote{position:static;font-style:italic}
.news .person{position:static;margin-top:6px}
.list{left:803px;top:703px;width:129px;list-style:none}
.list li{height:20.3px;line-height:17px;font-size:7.5px;color:#666;border-bottom:1px solid var(--line);padding-left:13px;position:relative}
.list li::before{content:"»";position:absolute;left:0;top:-1px;color:var(--accent);font-size:9px}
.link{font-size:6.5px;color:var(--muted);text-decoration:underline;letter-spacing:.3px}

/* footer */
.footer{left:0;top:950px;width:1200px;height:50px;background:var(--white);border-top:2px solid var(--line)}
.foot-text{top:969px;font-size:7px;color:var(--muted);letter-spacing:.2px}
</style>
</head>
<body>

<div class="abs hero" role="img" aria-label="Black and white office photo of a smiling businesswoman in front of a blurred team meeting"></div>
<div class="abs hero-portrait"></div>
<div class="abs brand hero-brand"><span class="brand-dot"></span><span class="brand-name">CREWLINE PARTNERS GLOBAL</span></div>
<div class="abs hero-title">Strive to be the best at <b>helping employers</b><br>achieve success through people</div>
<svg class="abs hero-arrows" width="40" height="22" viewBox="0 0 40 22"><path d="M10 2 L4 11 L10 20" fill="none" stroke="#fff" stroke-width="3"/><path d="M26 2 L32 11 L26 20" fill="none" stroke="#fff" stroke-width="3"/></svg>

<div class="abs navbar"></div>
<div class="abs brand nav-brand"><span class="brand-dot"></span><span class="brand-name">CREWLINE PARTNERS GLOBAL</span></div>
<nav class="abs nav">
  <a class="active" style="width:60px" href="#">HOME</a>
  <a style="width:80px" href="#">ABOUT US</a>
  <a style="width:67px" href="#">SERVICES</a>
  <a style="width:70px" href="#">CONTACT US</a>
</nav>
<span class="abs social" style="left:924px"></span>
<span class="abs social" style="left:944px"></span>
<div class="abs nav-tab-foot"></div>

<div class="abs partners"></div>
<svg class="abs" style="left:252px;top:366px" width="10" height="16"><path d="M8 1 L2 8 L8 15" fill="none" stroke="#ccc" stroke-width="1.5"/></svg>
<svg class="abs" style="left:951px;top:366px" width="10" height="16"><path d="M2 1 L8 8 L2 15" fill="none" stroke="#ccc" stroke-width="1.5"/></svg>
<div class="abs partner-row" role="img" aria-label="Row of client company badges">
  <span class="partner" style="width:14px"></span><span class="partner" style="width:14px"></span><span class="partner" style="width:22px"></span><span class="partner" style="width:18px"></span><span class="partner" style="width:20px"></span><span class="partner" style="width:16px"></span><span class="partner" style="width:12px"></span><span class="partner" style="width:12px"></span><span class="partner" style="width:26px"></span><span class="partner" style="width:32px"></span><span class="partner" style="width:14px"></span><span class="partner" style="width:14px"></span><span class="partner" style="width:22px"></span><span class="partner" style="width:18px"></span><span class="partner" style="width:20px"></span><span class="partner" style="width:14px"></span><span class="partner" style="width:22px"></span><span class="partner" style="width:20px"></span><span class="partner" style="width:14px"></span><span class="partner" style="width:22px"></span><span class="partner" style="width:18px"></span><span class="partner" style="width:20px"></span><span class="partner" style="width:14px"></span><span class="partner" style="width:16px"></span><span class="partner" style="width:26px"></span>
</div>

<section class="abs welcome">
  <h1>WELCOME TO OUR SITE!</h1>
  <p>Crewline Partners Global, popularly known as BWK, established in Doha, State of Qatar, is one of the pioneers of local and overseas recruitment along with manpower placements.</p>
</section>

<section class="abs features"></section>
<div class="abs feature-frame"><div class="feature-image" role="img" aria-label="Black and white globe on a textured background"></div></div>
<div class="abs feature" style="left:457px;top:521px;width:140px"><h2>People</h2><p>Our employees are efficient, motivated, honest, determined, result-driven and action-oriented.</p></div>
<div class="abs feature" style="left:653px;top:521px;width:130px"><h2>Service</h2><p>We aim for excellence through serving others and going above and beyond the call of duty.</p></div>
<div class="abs feature" style="left:833px;top:521px;width:130px"><h2>Peformance</h2><p>This organization was started with the aim to excel in the field of recruitment.</p></div>
<span class="abs read-more" style="left:457px;top:610px">READ MORE</span>
<span class="abs read-more" style="left:653px;top:610px">READ MORE</span>
<span class="abs read-more" style="left:834px;top:610px">READ MORE</span>
<span class="abs vrule" style="left:618px"></span>
<span class="abs vrule" style="left:804px"></span>

<div class="abs col-title" style="left:254px;top:675px">
  <svg width="16" height="12"><ellipse cx="8" cy="5" rx="7.5" ry="4.5" fill="#999"/><path d="M3 8 L2 12 L7 9Z" fill="#999"/></svg>Client Testimonials</div>
<div class="abs col-title" style="left:514px;top:675px">
  <svg width="12" height="12"><circle cx="4" cy="4" r="2.5" fill="#888"/><path d="M5 5 L10 11" stroke="#888" stroke-width="1.5"/></svg>News &amp; Events</div>
<div class="abs col-title" style="left:801px;top:675px">
  <svg width="14" height="14"><circle cx="6" cy="5" r="4" fill="none" stroke="#aaa"/><rect x="4" y="9" width="4" height="3" fill="#aaa"/></svg>Latest Companies</div>

<div class="abs card" style="top:700px"><span class="avatar" role="img" aria-label="Client portrait"></span><p class="quote">“Lorem ipsum dolor sit amet, consectetur adipi-sicing elit”</p><p class="person">Dana Whitfield, Social Media</p></div>
<div class="abs card" style="top:770px"><span class="avatar" role="img" aria-label="Client portrait"></span><p class="quote">“Lorem ipsum dolor sit amet, consectetur adipi-sicing elit, sed do”</p><p class="person">Dana Whitfield, Social Media</p></div>
<div class="abs card" style="top:840px"><span class="avatar" role="img" aria-label="Client portrait"></span><p class="quote">“Lorem ipsum dolor sit ametdo eiusmod tempor incididunt”</p><p class="person">Dana Whitfield, Social Media</p></div>
<a class="abs link" style="left:254px;top:927px">VIEW ALL &gt;&gt;</a>

<div class="abs date" style="top:700px"><b>12</b><span>JULY</span></div>
<div class="abs news" style="top:712px"><p class="quote">“Lorem ipsum dolor sit amet, consectetur adipi-sicing elit, sed do incididunt”</p><p class="person">Dana Whitfield</p></div>
<div class="abs date" style="top:770px"><b>13</b><span>JULY</span></div>
<div class="abs news" style="top:782px"><p class="quote">“Lorem ipsum dolor sit amet, consectetur adipi tempor incididunt”</p><p class="person">Dana Whitfield</p></div>
<div class="abs date" style="top:840px"><b>14</b><span>JULY</span></div>
<div class="abs news" style="top:852px"><p class="quote">“Lorem ipsum dolor sit amet, consectetur adipi tempor incididunt”</p><p class="person">Dana Whitfield</p></div>
<a class="abs link" style="left:515px;top:927px;text-decoration:none">VIEW ALL NEWS &gt;&gt;</a>

<ul class="abs list">
  <li>Strategic management</li>
  <li>Operations management</li>
  <li>Organizational Psychology</li>
  <li>Organizational development</li>
  <li>Root cause analysis</li>
  <li>Cause-and-effect analysis</li>
  <li>Benchmarking</li>
  <li>Statistical Process Control</li>
  <li>Performance metrics</li>
</ul>
<a class="abs link" style="left:803px;top:900px;text-decoration:none">MORE &gt;&gt;</a>

<footer class="abs footer"></footer>
<p class="abs foot-text" style="left:253px">COMPANY NAME &nbsp;|&nbsp; PRIVACY POLICY</p>
<p class="abs foot-text" style="right:240px">ABOUT US &nbsp;|&nbsp; TESTIMONIALS &nbsp;|&nbsp; OUR STAFF &nbsp;|&nbsp; EVENTS &amp; PRESS &nbsp;|&nbsp; CONTACT US</p>

</body>
</html>
```